National online rug retailer needs a home page design

See the LoomNest logo and create a home page design around that color theme. Details are spelled out in word document uploaded below.
Updates

Apparently this website did not take my attachement showing the logo and basic requirements.  If you would send me your email address, I will send you the attachment directly.
Best regards,
Ned Carver
ncarver@qwplex.com

Target Market(s)

The target market is home owners 25 to 75 years old with combined incomes over $100,000 per year.

Industry/Entity Type

Online

Requirements
Must have
• Lots of white space with black letters and creative use of red and possibly one other color. Would like a compelling call to action button.

```html
<!DOCTYPE html>
<html lang="en">
<head>
<meta charset="utf-8">
<title>LoomNest.com – Home</title>
<link href="https://fonts.googleapis.com/css2?family=Raleway:wght@400;500;600&family=Open+Sans:wght@400;600;700&family=Roboto+Slab:wght@700&family=Roboto+Condensed:wght@400;700&display=swap" rel="stylesheet">
<style>
:root{
  --red:#d71920;
  --red-dark:#b3121a;
  --ink:#333333;
  --grey:#8a8a8a;
  --light:#ededed;
  --line:#dcdcdc;
  --footer-bg:#f4f2ee;
  --white:#ffffff;
}
*{box-sizing:border-box;margin:0;padding:0}
html,body{width:847px;height:1200px;overflow:hidden;background:var(--white)}
body{position:relative;font-family:"Open Sans",sans-serif;color:var(--ink)}
.abs{position:absolute}
a{color:inherit;text-decoration:none}

/* header */
.topbar{top:14px;left:486px;display:flex;align-items:center;gap:12px;font:400 8.5px "Raleway",sans-serif;color:#666}
.topbar .sep{color:#ccc}
.topbar .count{color:var(--red)}
.checkout{background:var(--red);color:var(--white);border:2px solid var(--white);outline:1px solid var(--red);padding:3px 7px;border-radius:3px;font-weight:600;display:flex;align-items:center;gap:3px}
.logo{top:28px;left:92px;display:flex;align-items:center;gap:6px}
.logo-mark{width:14px;height:14px;background:var(--red)}
.logo-name{font:500 33px "Raleway",sans-serif;color:var(--red);letter-spacing:-.5px}
.tagline{top:67px;left:158px;font:400 8.5px "Raleway",sans-serif;color:#666}
.search{top:54px;left:316px;width:228px;height:19px;border:1px solid #cfcfcf;background:#f7f7f7;display:flex;align-items:center;justify-content:space-between;padding:0 7px;font-size:7.5px;color:#999}
.account{top:59px;left:562px;font:400 8px "Raleway",sans-serif;color:#555}
.chat{top:52px;left:663px;font:500 8.5px "Raleway",sans-serif;color:#444;line-height:15px}
.chat .online{color:#3ea82a;display:flex;align-items:center;gap:3px}
.chat .dot{width:8px;height:8px;border-radius:50%;background:#3ea82a}
.agent{top:36px;left:708px;width:46px;height:54px;background:linear-gradient(#e8ddd3,#f4f4f4);border-radius:4px}

.nav{top:90px;left:92px;width:662px;height:27px;background:linear-gradient(var(--red),var(--red-dark));border-radius:3px;display:flex;align-items:center;justify-content:space-around;font:500 10px "Raleway",sans-serif;color:var(--white)}
.nav span+span{border-left:1px solid rgba(255,255,255,.3);padding-left:22px}

.browse-title{top:126px;left:92px;font:500 14px "Raleway",sans-serif;color:#444}
.tollfree{top:126px;left:589px;font:400 12px "Raleway",sans-serif;color:#777;display:flex;align-items:center;gap:4px}
.tollfree b{color:var(--red);font-weight:500;letter-spacing:-.4px}

/* sidebar */
.sidebar{top:152px;left:94px;width:160px;height:346px;background:#f2f2f2;border:2px solid #e4e4e4;box-shadow:0 0 3px rgba(0,0,0,.1);padding:8px 12px;font-family:"Raleway",sans-serif;font-style:italic}
.sidebar .group{font-size:10px;color:#777;padding:5px 0 4px;border-bottom:1px solid #dadada}
.sidebar .item{font-size:8.5px;color:#999;padding:4px 0 3px 8px;border-bottom:1px solid #dadada}
.sidebar .gap{height:9px}

/* hero */
.hero{top:153px;left:266px;width:488px;height:229px;border:3px solid #e6e6e6;box-shadow:0 3px 6px rgba(0,0,0,.2);background:linear-gradient(170deg,#6b5a4a 0%,#3b2a22 25%,#d8cbb8 45%,#efe6d7 55%,#c9462e 75%,#a72b1f 100%)}
.hero-title{position:absolute;left:10px;bottom:8px;color:#222;font:500 16px "Raleway",sans-serif;line-height:18px}
.hero-title strong{display:block;font:700 24px "Roboto Slab",serif;color:var(--red)}
.also{top:394px;left:266px;font:400 11px "Raleway",sans-serif;color:var(--red)}
.thumb{top:414px;width:106px;height:83px;border:4px solid var(--red)}
.arrow{top:443px}
.dotted{top:518px;left:154px;width:540px;border-top:1px dotted #bbb}

/* kitchen promo */
.promo{top:534px;left:92px;width:663px;height:60px;border:1px solid #cfcfcf;background:var(--white)}
.promo-img{position:absolute;left:2px;top:2px;width:98px;height:54px;background:linear-gradient(120deg,#b22 0%,#333 50%,#555 100%);border-radius:4px}
.promo-tag{position:absolute;left:101px;top:0;width:28px;height:30px;background:#f26b1d;color:var(--white);font:700 6px "Open Sans",sans-serif;text-align:center;line-height:7px;padding-top:3px}
.promo-head{position:absolute;left:141px;top:15px;font:700 14px "Roboto Condensed",sans-serif;color:#222;line-height:14px}
.promo-head span{display:block;font-weight:400;font-size:10px;color:#333}
.promo-price{position:absolute;left:330px;top:26px;font:400 9px "Roboto Condensed",sans-serif;color:#333}
.promo-price b{font-size:15px}
.buy{position:absolute;left:404px;top:25px;width:62px;height:16px;background:linear-gradient(#f47a2a,#d8501a);border-radius:2px;color:var(--white);font:700 8px "Open Sans",sans-serif;text-align:center;line-height:16px}
.promo-note{position:absolute;left:485px;top:26px;font:700 5.5px "Open Sans",sans-serif;color:#444;line-height:8px}
.promo-brand{position:absolute;left:595px;top:15px;font:600 13px "Raleway",sans-serif;color:var(--red)}

/* featured */
.featured{top:608px;left:92px;font:500 13px "Raleway",sans-serif;color:#444}
.featured-line{top:618px;left:212px;width:543px;border-top:1px solid #e2e2e2}
.product{width:120px}
.product .pic{height:96px;border:4px solid #a9a9a9}
.product h3{margin-top:10px;font:400 11px "Raleway",sans-serif;color:var(--red)}
.product p{margin-top:3px;font:400 7px "Open Sans",sans-serif;color:#999;line-height:10.5px}
.fur{background:linear-gradient(160deg,#5c4a3a,#eee5d5 45%,#d9cbb5 70%,#3a2a20)}
.modern{background:linear-gradient(160deg,#6b5645,#b9aa98 40%,#8d8276 60%,#6a5d52)}
.trad{background:linear-gradient(135deg,#e0a01e,#c3331f 45%,#2d4a86 70%,#d9751d)}
.fancy{background:linear-gradient(170deg,#ddd 0%,#f2f2ef 40%,#7c9a3c 60%,#e7e3d6)}
.casual{background:linear-gradient(160deg,#6b5645,#b9aa98 40%,#8d8276 60%,#6a5d52)}

/* footer */
.footer{top:968px;left:0;width:847px;height:186px;background:var(--footer-bg)}
.fcol{top:984px;font-family:"Raleway",sans-serif}
.fcol h4{font:400 12px "Raleway",sans-serif;color:var(--red);margin-bottom:14px;line-height:14px}
.fcol li{list-style:none;font-size:8.5px;color:#777;line-height:12.9px}
.fdiv{top:990px;width:1px;height:145px;background:#e0dcd5}
.signup-input{top:1015px;left:572px;width:182px;height:20px;border:1px solid #c8c8c8;border-radius:3px;background:var(--white);font-size:7.5px;color:#999;padding:5px 9px}
.submit{top:1044px;left:704px;width:50px;height:18px;background:var(--red);border-radius:2px;color:var(--white);font:700 8px "Open Sans",sans-serif;text-align:center;line-height:18px}
.card{width:24px;height:15px;background:#e4e4e4;border:1px solid #cfcfcf;border-radius:2px}
.badge{background:#d8d2c2;border-radius:50%}
.copy-bar{top:1154px;left:0;width:847px;height:46px;background:var(--red)}
.copy{top:1171px;left:92px;font:400 9px "Raleway",sans-serif;color:var(--white)}
.footer-logo{top:1162px;left:640px;font:500 20px "Raleway",sans-serif;color:rgba(255,255,255,.35)}
</style>
</head>
<body>

<header>
  <div class="abs topbar">
    <span>ITEMS: <span class="count">12</span></span><span class="sep">|</span>
    <span>TOTAL: $0.00</span><span class="sep">|</span>
    <span>VIEW CART</span><span class="sep">|</span>
    <a class="checkout" href="#"><svg width="8" height="8" viewBox="0 0 8 8"><circle cx="4" cy="4" r="4" fill="#fff"/><path d="M3 2l3 2-3 2z" fill="#d71920"/></svg>CHECKOUT</a>
  </div>
  <div class="abs logo"><span class="logo-mark"></span><span class="logo-name">LoomNest.com</span></div>
  <div class="abs tagline">for domestic and heirloom values</div>
  <div class="abs search"><span>Enter key words or item #</span>
    <svg width="10" height="10" viewBox="0 0 10 10"><circle cx="4" cy="4" r="3" fill="none" stroke="#555" stroke-width="1.3"/><path d="M6.3 6.3L9 9" stroke="#555" stroke-width="1.5"/></svg></div>
  <div class="abs account">My Account &nbsp;|&nbsp; Sign In</div>
  <div class="abs chat">LIVE CHAT<div class="online"><span class="dot"></span>Online</div></div>
  <div class="abs agent" role="img" aria-label="Support agent with headset"></div>
  <nav class="abs nav"><span>Home</span><span>Selection Guides</span><span>Rug Care</span><span>FAQ</span><span>Return Policy</span><span>Free Shipping</span><span>Clearance Rugs</span></nav>
</header>

<div class="abs browse-title">BROWSE</div>
<div class="abs tollfree"><svg width="8" height="12" viewBox="0 0 8 12"><path d="M6 1C2 2 1 5 1 6s1 4 5 5" fill="none" stroke="#d71920" stroke-width="2"/></svg>Order Toll-Free: <b>1-888-555-0142</b></div>

<aside class="abs sidebar">
  <div class="group">Rug Theme ::::</div>
  <div class="item">Traditional</div><div class="item">Transitional</div><div class="item">Casual</div>
  <div class="gap"></div>
  <div class="group">Color Way ::::</div>
  <div class="item">Black</div><div class="item">Blue</div><div class="item">Green</div><div class="item">Gold</div>
  <div class="gap"></div>
  <div class="group">Size ::::</div>
  <div class="group">Shape ::::</div>
  <div class="group">Fiber Content ::::</div>
  <div class="group">MFGR. Brand ::::</div>
  <div class="group">MFGR. Collection ::::</div>
  <div class="group">Price ::::</div>
</aside>

<section class="abs hero" role="img" aria-label="Stack of folded shag and woven rugs">
  <div class="hero-title">SPECIALIZING IN<strong>UNIQUE RUGS</strong></div>
</section>

<div class="abs also">You May Also Like:</div>
<svg class="abs arrow" style="left:268px" width="10" height="20" viewBox="0 0 10 20"><path d="M9 0L0 10l9 10z" fill="#ccc"/></svg>
<div class="abs thumb fur" style="left:288px" role="img" aria-label="White fur rug"></div>
<div class="abs thumb modern" style="left:400px" role="img" aria-label="Modern pebble rug"></div>
<div class="abs thumb trad" style="left:512px" role="img" aria-label="Traditional patterned rug"></div>
<div class="abs thumb fancy" style="left:624px" role="img" aria-label="Rug in living room with sofa"></div>
<svg class="abs arrow" style="left:740px" width="10" height="20" viewBox="0 0 10 20"><path d="M1 0l9 10-9 10z" fill="#999"/></svg>
<div class="abs dotted"></div>

<section class="abs promo">
  <div class="promo-img" role="img" aria-label="Frying pan and grill pan"></div>
  <div class="promo-tag">UPTO<br>50%<br>off</div>
  <div class="promo-head">KITCHEN SALE<span>Largest selection of Kitchen Appliances</span></div>
  <div class="promo-price">Starting <b>₹ 199</b></div>
  <a class="buy" href="#">Buy Now</a>
  <div class="promo-note">• MANUFACTURER WARRANTY<br>• FREE SHIPPING</div>
  <div class="promo-brand">HomeMart</div>
</section>

<div class="abs featured">Featured Products:</div>
<div class="abs featured-line"></div>

<div class="abs product" style="top:631px;left:92px"><div class="pic fur" role="img" aria-label="Fur rug"></div><h3>FUR RUGS</h3><p>Lorem Ipsum is simply dummy text of the printing and type...</p></div>
<div class="abs product" style="top:631px;left:228px"><div class="pic modern" role="img" aria-label="Modern rug"></div><h3>MODERN RUGS</h3><p>Lorem Ipsum is simply dummy text of the printing and type...</p></div>
<div class="abs product" style="top:631px;left:364px"><div class="pic trad" role="img" aria-label="Traditional rug"></div><h3>TRADITIONAL RUGS</h3><p>Lorem Ipsum is simply dummy text of the printing and type...</p></div>
<div class="abs product" style="top:631px;left:499px"><div class="pic fancy" role="img" aria-label="Fancy rug"></div><h3>FANCY RUGS</h3><p>Lorem Ipsum is simply dummy text of the printing and type...</p></div>
<div class="abs product" style="top:631px;left:634px"><div class="pic casual" role="img" aria-label="Casual rug"></div><h3>CASUAL RUGS</h3><p>Lorem Ipsum is simply dummy text of the printing and type...</p></div>

<div class="abs product" style="top:788px;left:92px"><div class="pic fur" role="img" aria-label="Fur rug"></div><h3>FUR RUGS</h3><p>Lorem Ipsum is simply dummy text of the printing and type...</p></div>
<div class="abs product" style="top:788px;left:228px"><div class="pic modern" role="img" aria-label="Modern rug"></div><h3>MODERN RUGS</h3><p>Lorem Ipsum is simply dummy text of the printing and type...</p></div>
<div class="abs product" style="top:788px;left:364px"><div class="pic trad" role="img" aria-label="Traditional rug"></div><h3>TRADITIONAL RUGS</h3><p>Lorem Ipsum is simply dummy text of the printing and type...</p></div>
<div class="abs product" style="top:788px;left:499px"><div class="pic fancy" role="img" aria-label="Fancy rug"></div><h3>FANCY RUGS</h3><p>Lorem Ipsum is simply dummy text of the printing and type...</p></div>
<div class="abs product" style="top:788px;left:634px"><div class="pic casual" role="img" aria-label="Casual rug"></div><h3>CASUAL RUGS</h3><p>Lorem Ipsum is simply dummy text of the printing and type...</p></div>

<footer>
  <div class="abs footer"></div>
  <div class="abs fcol" style="left:92px"><h4>Customer Service</h4><ul>
    <li>Shipping</li><li>Return Policy</li><li>Privacy Policy</li><li>Ordering &amp; Delivery Checklist</li><li>Terms of Use</li><li>Terms of Sale</li><li>Contact Us</li><li>Environmental Policy</li></ul></div>
  <div class="abs fdiv" style="left:232px"></div>
  <div class="abs fcol" style="left:272px"><h4>Resources</h4><ul>
    <li>Product Articles</li><li>Learning Center</li><li>Help</li><li>Refer A Friend</li><li>LoomNest Blog</li><li>Room Scene Viewer</li><li>Site Map</li><li>FAQ</li><li>Customer Testimonials</li><li>Photo Gallery</li></ul></div>
  <div class="abs fdiv" style="left:390px"></div>
  <div class="abs fcol" style="left:420px"><h4>Corporate Info</h4><ul>
    <li>About LoomNest.com</li><li>Careers</li><li>Affiliates</li></ul></div>
  <div class="abs fcol" style="left:571px"><h4>Sign up for Daily Fair Deals.<br>Don't miss out!</h4></div>
  <div class="abs signup-input">Enter Your Email Address</div>
  <a class="abs submit" href="#">SUBMIT</a>

  <div class="abs card" style="top:1079px;left:422px"></div>
  <div class="abs card" style="top:1079px;left:451px"></div>
  <div class="abs card" style="top:1079px;left:479px"></div>
  <div class="abs card" style="top:1105px;left:422px"></div>
  <div class="abs card" style="top:1105px;left:451px"></div>
  <div class="abs card" style="top:1105px;left:479px"></div>

  <div class="abs badge" style="top:1073px;left:609px;width:32px;height:32px"></div>
  <div class="abs badge" style="top:1073px;left:663px;width:32px;height:32px"></div>
  <div class="abs" style="top:1078px;left:704px;width:44px;height:18px;background:#e2ddd2;border-radius:2px"></div>
  <div class="abs" style="top:1112px;left:627px;width:45px;height:24px;background:#e2ddd2;border-radius:2px"></div>
  <div class="abs" style="top:1112px;left:681px;width:44px;height:24px;background:#d5dae4;border-radius:2px"></div>

  <div class="abs copy-bar"></div>
  <div class="abs copy">©1998-2013 LoomNest.com Inc. All rights reserved.</div>
  <div class="abs footer-logo">LoomNest.com</div>
</footer>

</body>
</html>
```